Agriculture Technology Website Design Project

We need a new website for a company called Brook Ledger Works. We have a document laid out with all of the requirements (see below) and would like you to follow the instructions on there. In this document, there is all of the copy that must be included on the website and what order it should go in as well as images. These images have specific names and are listed in the document as to where they should go. Please make this one continuous site that users can easily scroll through. We would like it to be sleek and modern with as little clutter as possible. Please refer to the brochure that we have posted below (Stone Analytica.pdf) for a design we have had done for the company in the past. We really like this design and it would be great if the color scheme was similar on the website.

Industry/Entity Type

Agriculture

Number of Pages Required

1 page

Font styles to use
Sans Serif

```html
<!DOCTYPE html>
<html lang="en">
<head>
<meta charset="utf-8">
<title>Brook Ledger Works</title>
<link rel="stylesheet" href="https://fonts.googleapis.com/css2?family=Open+Sans:wght@400;600;700;800&family=Roboto:wght@300;400;500&family=Lato:wght@400;700&display=swap">
<style>
:root{
  --green:#5dbb7a;
  --green-dark:#3f9e5d;
  --ink:#222;
  --text:#444;
  --muted:#666;
  --light:#f3f3f3;
  --white:#fff;
  --footer:#121414;
  --footer-bar:#262828;
  --blue:#1a6aa8;
}
*{box-sizing:border-box;margin:0;padding:0}
html,body{width:1200px;height:2726px;overflow:hidden;background:var(--white)}
body{position:relative;font-family:'Roboto',sans-serif;color:var(--text)}
section,header,footer{position:absolute;left:0;width:1200px}
.abs{position:absolute}

/* nav */
.site-header{top:0;height:72px;background:var(--white);border-bottom:1px solid #e4e4e4}
.brand{left:161px;top:14px;display:flex;align-items:center;gap:8px;font:700 13px 'Open Sans',sans-serif;color:var(--green-dark)}
.brand-mark{width:16px;height:16px;border-radius:50%;background:var(--green-dark)}
.nav{right:0;top:0;left:571px;display:flex;height:72px}
.nav a{display:block;height:72px;line-height:72px;padding:0 16px;font:400 13px 'Roboto',sans-serif;color:#555;text-decoration:none}
.nav a.active{background:var(--green);color:var(--white);padding:0 17px}

/* hero */
.hero{top:72px;height:440px;background:linear-gradient(180deg,#6f8fae 0%,#94a9b6 35%,#5f6e58 60%,#8a8b7c 85%,#a59a84 100%)}
.hero-title{top:122px;width:100%;text-align:center;font:700 54px 'Open Sans',sans-serif;color:var(--white);letter-spacing:-.5px}
.hero-sub{top:198px;width:100%;text-align:center;font:400 19px 'Open Sans',sans-serif;color:var(--white)}
.btn{display:inline-block;font:500 12px 'Roboto',sans-serif;text-transform:uppercase;text-decoration:none;text-align:center}
.hero .btn{top:288px;height:43px;line-height:43px;width:136px}
.btn-light{background:var(--white);color:var(--green-dark)}
.btn-green{background:var(--green);color:var(--white)}

/* services */
.services{top:512px;height:321px}
.card{top:48px;width:209px;height:225px;background:var(--white);box-shadow:0 2px 6px rgba(0,0,0,.15);text-align:center;padding-top:29px}
.card h3{font:500 12.5px/18px 'Roboto',sans-serif;color:var(--ink);letter-spacing:.3px;text-transform:uppercase}
.card .rule{width:32px;height:2px;background:var(--green);margin:9px auto 0}
.card p{font:300 13px/19px 'Roboto',sans-serif;color:var(--muted);margin:21px 14px 0;height:57px}
.card .btn{margin-top:19px;width:113px;height:29px;line-height:27px;border:1px solid var(--green-dark);color:var(--green-dark);font-size:10.5px}
.card .btn.filled{background:var(--green);border-color:var(--green);color:var(--white)}
.card .btn::after{content:"  \2192"}
.card.contact{background:linear-gradient(160deg,#4fb27a 0%,#2b8a9a 55%,#1766aa 100%);box-shadow:none}
.card.contact h3,.card.contact p{color:var(--white)}
.card.contact .rule{background:var(--white)}
.card.contact p{font-size:13px;margin-top:20px;height:auto}
.card.contact .phone{font:400 21px 'Roboto',sans-serif;color:var(--white);margin-top:14px}
.card.contact .btn{background:var(--white);color:var(--green-dark);border-color:var(--white);margin-top:20px}

/* about */
.about{top:833px;height:547px;background:var(--light)}
.about h2{left:160px;top:86px;font:800 36px 'Open Sans',sans-serif;color:#111;letter-spacing:.5px}
.about .kicker{left:160px;top:135px;font:700 19px 'Open Sans',sans-serif;color:var(--green)}
.about .body{left:161px;top:189px;width:295px;font:400 15.5px/26.3px 'Lato',sans-serif;color:var(--ink)}
.photo{background:linear-gradient(180deg,#9ec3e4 0%,#5f7f3e 30%,#4c6e31 60%,#a08e72 85%,#c2ae8f 100%)}
.about .photo{left:504px;top:61px;width:318px;height:428px}
.goal{left:855px;top:130px;font:700 31px 'Open Sans',sans-serif;color:var(--green)}
.goal-text{left:856px;top:211px;width:280px;font:400 26px/39px 'Open Sans',sans-serif;color:#333}
.about .btn{left:857px;top:375px;width:136px;height:43px;line-height:43px}

/* why */
.why{top:1380px;height:497px}
.why h2{left:162px;top:48px;font:700 27px 'Open Sans',sans-serif;color:#111}
.why .kicker{left:162px;top:93px;font:400 22px 'Open Sans',sans-serif;color:var(--green)}
.why .body{left:161px;top:149px;width:420px;font:400 17px/26.5px 'Lato',sans-serif;color:var(--ink)}
.why .body p{margin-bottom:26px}
.why .btn{left:161px;top:395px;width:136px;height:43px;line-height:43px}
.why .photo{left:622px;top:56px;width:417px;height:382px;background:radial-gradient(circle at 50% 40%,#c6d96a 0%,#a8c147 40%,#8ea66a 75%,#b6c0a6 100%)}

/* testimonials */
.testimonials{top:1877px;height:414px;background:var(--light)}
.testimonials h2{top:70px;width:100%;text-align:center;padding-right:34px;font:400 24px 'Open Sans',sans-serif;color:#444;letter-spacing:.6px}
.arrow-btn{width:31px;height:31px;border-radius:50%;border:1px solid #ccc;background:var(--white);display:flex;align-items:center;justify-content:center}
.testimonials .arrow-btn{top:150px}
.avatar{border-radius:50%;border:3px solid var(--white)}
.av-side{top:135px;width:60px;height:60px;background:#d9c8b6}
.av-main{left:566px;top:126px;width:74px;height:74px;background:#8a7a6d}
.quote-badge{left:586px;top:190px;width:26px;height:26px;border-radius:50%;background:var(--green);border:2px solid var(--white)}
.quote{left:305px;top:250px;width:590px;text-align:center;font:300 12.5px/19.5px 'Roboto',sans-serif;color:#555}
.byline{top:327px;width:100%;text-align:center;font:300 12.5px 'Roboto',sans-serif;color:#777}
.byline b{font-weight:500;color:#333}

/* partners */
.partners{top:2291px;height:138px}
.partners .arrow-btn{top:54px}
.partner{top:58px;font:700 22px 'Open Sans',sans-serif;color:#333;text-align:center}
.partner-badge{display:inline-block;width:14px;height:14px;background:#333;margin-right:8px;vertical-align:-1px}

/* footer */
.site-footer{top:2429px;height:297px;background:var(--footer)}
.fcol{top:48px}
.fcol h4{font:500 15px 'Roboto',sans-serif;color:var(--white)}
.fcol .rule{width:37px;height:2px;background:#1e5fb0;margin-top:10px}
.fcol p{font:400 10.5px/17.5px 'Roboto',sans-serif;color:#bbb;width:165px;margin-top:14px}
.fcol ul{list-style:none;margin-top:21px}
.fcol li{font:400 11px 'Roboto',sans-serif;color:#bbb;height:26.5px;padding-left:12px;position:relative}
.fcol li::before{content:"";position:absolute;left:0;top:4px;width:4px;height:4px;background:#bbb}
.fcol .info li{padding-left:22px;height:32px}
.fcol .info li::before{display:none}
.fcol .info svg{position:absolute;left:0;top:0}
.footer-bar{top:257px;height:40px;background:var(--footer-bar);font:400 11.5px 'Roboto',sans-serif;color:#bbb}
.footer-bar .copy{left:154px;top:13px}
.footer-bar .links{left:828px;top:13px}
.footer-bar u{color:var(--white)}
</style>
</head>
<body>

<header class="site-header">
  <div class="brand abs"><span class="brand-mark"></span>Brook Ledger Works</div>
  <nav class="nav abs">
    <a class="active">Home</a><a>About Us</a><a>Why BLW?</a><a>Products</a><a>Partners</a><a>Contact Us</a>
  </nav>
</header>

<section class="hero" role="img" aria-label="Irrigation filter station beside an orchard under a blue sky">
  <h1 class="hero-title abs">Brook Ledger Works</h1>
  <p class="hero-sub abs">Bringing industrial automation to the farm</p>
  <a class="btn btn-light abs" style="left:460px">Our Products</a>
  <a class="btn btn-green abs" style="left:604px;width:136px">About Us</a>
</section>

<section class="services">
  <div class="card abs" style="left:43px"><h3>Crop<br>Monitoring</h3><div class="rule"></div><p>Ensuring that you have real-time information to optimize irrigation managemen</p><a class="btn filled">Learn More</a></div>
  <div class="card abs" style="left:269px"><h3>Pump Monitoring<br>and Control</h3><div class="rule"></div><p>Scalable and cost-effective pump monitoring with built-in remote control</p><a class="btn">Learn More</a></div>
  <div class="card abs" style="left:495px"><h3>Irrigation<br>Automation</h3><div class="rule"></div><p>Upgrade your irrigation system: from retrofit to ranch-wide automation</p><a class="btn">Learn More</a></div>
  <div class="card abs" style="left:721px"><h3>Control Panel<br>Design and Build</h3><div class="rule"></div><p>Leverage BLW design and build expertise to meet your exact needs and specifications</p><a class="btn">Learn More</a></div>
  <div class="card contact abs" style="left:948px"><h3>Contact Us</h3><div class="rule"></div><p>For immediate support call</p><div class="phone">(555 204 - 7718)</div><a class="btn">Get in Touch</a></div>
</section>

<section class="about">
  <h2 class="abs">ABOUT US</h2>
  <div class="kicker abs">BLW is a Systems Integrator</div>
  <p class="body abs">Our focus is on helping California growers design, build and adopt effective irrigation management solutions. Our team has worked together for over 15 years, providing monitoring and control systems for 60+ crops that have successfully helped over 500 farms significantly improve irrigation management. We also farm our own 200 acre technology lab to help ensure we deliver reliable monitoring and automation to your farm.</p>
  <div class="photo abs" role="img" aria-label="Filter tanks and pipes at the edge of an orchard"></div>
  <div class="goal abs">OUR GOAL</div>
  <p class="goal-text abs">to be your trusted partner for technology adoption</p>
  <a class="btn btn-green abs">Our Products</a>
</section>

<section class="why">
  <h2 class="abs">Why BLW?:</h2>
  <div class="kicker abs">We're your local farm data team.</div>
  <div class="body abs">
    <p>We are experts at deploying Information Technology for irrigation management.</p>
    <p>We partner with our customers to deliver the right solutions.</p>
    <p>&nbsp;Everything we sell is off-the-shelf, cost-effective and reliable.</p>
  </div>
  <a class="btn btn-green abs">Get in Touch</a>
  <div class="photo abs" role="img" aria-label="Bunches of green grapes on the vine"></div>
</section>

<section class="testimonials">
  <h2 class="abs">What Client Say...</h2>
  <div class="arrow-btn abs" style="left:407px"><svg width="8" height="8" viewBox="0 0 8 8"><path d="M5 1L2 4l3 3" fill="none" stroke="#888"/></svg></div>
  <div class="arrow-btn abs" style="left:762px"><svg width="8" height="8" viewBox="0 0 8 8"><path d="M3 1l3 3-3 3" fill="none" stroke="#888"/></svg></div>
  <div class="avatar av-side abs" style="left:522px" role="img" aria-label="Client portrait"></div>
  <div class="avatar av-side abs" style="left:620px" role="img" aria-label="Client portrait"></div>
  <div class="avatar av-main abs" role="img" aria-label="Featured client portrait"></div>
  <div class="quote-badge abs"></div>
  <p class="quote abs">"Sed ut perspiciatis unde omnis iste natus error sit voluptatem accusantium doloremque laudantium, totam rem aperiam, eaque ipsa quae ab illo inventore veritatis et quasi architecto beatae vitae dicta sunt explicabo."</p>
  <p class="byline abs">- by <b>Dana Wells</b></p>
</section>

<section class="partners">
  <div class="arrow-btn abs" style="left:147px"><svg width="8" height="8" viewBox="0 0 8 8"><path d="M5 1L2 4l3 3" fill="none" stroke="#888"/></svg></div>
  <div class="partner abs" style="left:215px;width:124px">Kestrel</div>
  <div class="partner abs" style="left:413px;width:156px">Marlow</div>
  <div class="partner abs" style="left:640px;width:80px"><span class="partner-badge"></span>Vantix</div>
  <div class="partner abs" style="left:800px;width:175px">Orchard Field</div>
  <div class="arrow-btn abs" style="left:1021px"><svg width="8" height="8" viewBox="0 0 8 8"><path d="M3 1l3 3-3 3" fill="none" stroke="#888"/></svg></div>
</section>

<footer class="site-footer">
  <div class="fcol abs" style="left:154px"><h4>BROOK LEDGER WORKS</h4><div class="rule"></div><p>Lorem Ipsum is simply dummy text of the printing and typesetting industry. Lorem Ipsum has been the industry's standard dummy text ever since the 1500s, when</p></div>
  <div class="fcol abs" style="left:379px"><h4>Experiences</h4><div class="rule"></div><ul><li>About Us</li><li>Why BLW?</li><li>Products</li><li>Partners</li><li>Contact Us</li></ul></div>
  <div class="fcol abs" style="left:604px"><h4>Follow Us</h4><div class="rule"></div><ul><li>Fieldnotes</li><li>Chirpline</li><li>Photoloom</li></ul></div>
  <div class="fcol abs" style="left:829px"><h4>Contact Info</h4><div class="rule"></div>
    <ul class="info">
      <li><svg width="12" height="12" viewBox="0 0 12 12"><rect x="1" y="3" width="10" height="7" fill="none" stroke="#bbb"/><path d="M1 3l5 4 5-4" fill="none" stroke="#bbb"/></svg>info@brookledgerworks.com</li>
      <li><svg width="12" height="12" viewBox="0 0 12 12"><path d="M3 1l2 3-1 1c1 2 2 3 3 3l1-1 3 2-1 2C5 11 1 7 1 3z" fill="#bbb"/></svg>555-204-7718</li>
      <li><svg width="12" height="12" viewBox="0 0 12 12"><circle cx="6" cy="6" r="5" fill="none" stroke="#bbb"/><path d="M1 6h10M6 1v10" stroke="#bbb"/></svg>www.brookledgerworks.com</li>
    </ul>
  </div>
  <div class="footer-bar abs" style="left:0;width:1200px">
    <span class="copy abs">© &nbsp;Copyright 2020 All Right Reserved.</span>
    <span class="links abs"><u>Privacy Statement</u> &nbsp;&nbsp; | &nbsp;&nbsp; Terms Of Use</span>
  </div>
</footer>

</body>
</html>
```